Seeking a beautiful packaging box for Dusk Haven - an essential oil blend (mock up provided!)

My sleep brand - Dusk Haven - is almost ready to go to market. And I need a box! Dusk Haven is a high end essential oils/sleep hygiene brand.

I need a gorgeous, classy box for our 3 sizes of essential oil product we are selling. I have a draft mockup which is to approximate size (attached), but need some help with the finishing touches and layout so it's really polished. I am looking for simple/monochrome designs using black and off white (think Verlin inspo!)

We are selling a 15mL dropper bottle and two roll ons (5ml, 10ml) of the essential oil blend. These are all amber bottles with black top. The box design will be almost identical for each, with very slight variations due to size differences.

The size of the boxes will be
15mL dropper: 30x30x95mm
10ml roller: 19x19x88mm
5ml roller: 18x18x59mm

Target Market(s)

High end/high price point product, shift workers, mums, people suffering stress and insomnia

Industry/Entity Type

Health And Wellness

Font styles to use
Serif
Sans Serif

Colors

Designer to choose only greyscale colors for use in the design.

Requirements
Must have
• I have attached a word document which includes all the necessary text:
- ingredients
- directions
- cautions
- info on essential oils/dusk haven (abbreviated on the smallest box)

Additionally:
- volume
- our website
- instagram logo/duskhavenau name
- made in australia
- recycle symbol
- 12 month open symbol
Nice to have
• I would like the boxes to be monochromatic: white or off white colour, with black logo and writing. I am open to variations on the logo (ie position of writing in relation to the circle/change of font size), but mostly need help with layout, font, direction of text, design of the blank spaces, patterns etc.
Should not have
• Colours

```html
<!DOCTYPE html>
<html lang="en">
<head>
<meta charset="utf-8">
<title>Dusk Haven – Essential Oil Blend Box Dielines</title>
<link rel="stylesheet" href="https://fonts.googleapis.com/css2?family=Cormorant+Garamond:wght@400;500&family=Crimson+Pro:ital,wght@0,400;0,600;0,700;1,400;1,600;1,700&display=swap">
<style>
  :root {
    --ink: #0d0d0d;
    --paper: #ffffff;
    --panel-light: #f6f6f4;
    --type-light: #f2f2f2;
    --type-dark: #111111;
    --rule: #777777;
  }
  * { box-sizing: border-box; margin: 0; padding: 0; }
  html, body { width: 1200px; height: 900px; overflow: hidden; background: var(--paper); }
  body { position: relative; font-family: "Crimson Pro", Georgia, serif; color: var(--type-light); }

  .dieline { position: absolute; background: var(--ink); }
  .dieline--15ml { left: 582px; top: 18px; width: 556px; height: 438px; }
  .dieline--10ml { left: 424px; top: 475px; width: 364px; height: 410px; }
  .dieline--5ml  { left: 804px; top: 569px; width: 368px; height: 273px; }

  .col { position: absolute; text-align: center; line-height: 1.1; }
  .col h3 { font-weight: 700; letter-spacing: .03em; text-transform: uppercase; }
  .col p { margin-bottom: 4px; }
  .col b { font-weight: 700; display: block; }

  .wordmark {
    position: absolute;
    writing-mode: vertical-rl;
    transform: rotate(180deg);
    font-family: "Cormorant Garamond", Georgia, serif;
    font-weight: 400;
    color: var(--type-light);
    white-space: nowrap;
  }
  .brand-dot {
    position: absolute; border-radius: 50%;
    border: 2px solid var(--type-light); background: var(--ink);
  }
  .info-panel {
    position: absolute; background: var(--panel-light); color: var(--type-dark);
    display: flex;
  }
  .info-panel__story { font-style: italic; text-align: center; line-height: 1.12; }
  .info-panel__story p { margin-bottom: 6px; }
  .info-panel__product { display: flex; flex-direction: column; justify-content: flex-end; }
  .product-title { font-weight: 600; line-height: 1; border-bottom: 1px solid var(--rule); padding-bottom: 2px; margin-bottom: 3px; }
  .product-sub { font-style: italic; line-height: 1.15; }
  .product-origin { margin-top: 8px; line-height: 1.25; }

  .notes i { font-weight: 700; display: block; }
  .caution { line-height: 1.1; }
  .marks { display: flex; justify-content: center; gap: 8px; align-items: center; }
  .mark-recycle { border-radius: 50%; border: 2px solid var(--type-light); }
  .mark-open { border: 2px solid var(--type-light); border-radius: 3px; }

  /* 15 mL */
  .dieline--15ml .col--ingredients { left: 8px; top: 14px; width: 134px; font-size: 11px; }
  .dieline--15ml .col--ingredients h3 { font-size: 12.5px; margin-bottom: 3px; }
  .dieline--15ml .wordmark { left: 150px; top: 14px; font-size: 20px; letter-spacing: 13px; }
  .dieline--15ml .brand-dot { left: 192px; top: 252px; width: 64px; height: 64px; }
  .dieline--15ml .info-panel { left: 11px; top: 297px; width: 255px; height: 126px; padding: 6px 6px; }
  .dieline--15ml .info-panel__story { width: 122px; font-size: 10.5px; }
  .dieline--15ml .info-panel__product { padding-left: 18px; width: 126px; padding-bottom: 4px; }
  .dieline--15ml .product-title { font-size: 13.5px; }
  .dieline--15ml .product-sub, .dieline--15ml .product-origin { font-size: 8.5px; }
  .dieline--15ml .col--directions { left: 284px; top: 14px; width: 128px; font-size: 10.5px; }
  .dieline--15ml .col--directions h3 { font-size: 12px; margin-bottom: 4px; }
  .dieline--15ml .col--about { left: 428px; top: 14px; width: 118px; font-size: 10.5px; }
  .dieline--15ml .col--about .brand-dot { position: relative; left: 0; top: 0; display: block; margin: 8px auto 10px; width: 58px; height: 58px; }

  /* 10 mL */
  .dieline--10ml .col--directions { left: 4px; top: 64px; width: 90px; font-size: 11px; }
  .dieline--10ml .col--directions h3 { font-size: 11px; }
  .dieline--10ml .wordmark { left: 94px; top: 22px; font-size: 18px; letter-spacing: 9px; }
  .dieline--10ml .brand-dot { left: 124px; top: 242px; width: 52px; height: 52px; }
  .dieline--10ml .info-panel { left: 7px; top: 270px; width: 162px; height: 124px; padding: 4px 4px; }
  .dieline--10ml .info-panel__story { width: 82px; font-size: 9.5px; }
  .dieline--10ml .info-panel__product { padding-left: 6px; width: 74px; }
  .dieline--10ml .product-title { font-size: 12px; }
  .dieline--10ml .product-sub, .dieline--10ml .product-origin { font-size: 7px; }
  .dieline--10ml .col--ingredients { left: 178px; top: 12px; width: 88px; font-size: 9.6px; }
  .dieline--10ml .col--ingredients h3 { font-size: 10px; }
  .dieline--10ml .col--about { left: 272px; top: 14px; width: 86px; font-size: 11px; }

  /* 5 mL */
  .dieline--5ml .col--directions { left: 4px; top: 6px; width: 78px; font-size: 8px; }
  .dieline--5ml .col--directions h3 { font-size: 8px; }
  .dieline--5ml .wordmark { left: 84px; top: 8px; font-size: 13px; letter-spacing: 5px; }
  .dieline--5ml .brand-dot { left: 116px; top: 120px; width: 42px; height: 42px; }
  .dieline--5ml .info-panel { left: 3px; top: 147px; width: 157px; height: 119px; padding: 4px 4px; }
  .dieline--5ml .info-panel__story { width: 78px; font-size: 7.6px; }
  .dieline--5ml .info-panel__product { padding-left: 8px; width: 72px; }
  .dieline--5ml .product-title { font-size: 10px; }
  .dieline--5ml .product-sub, .dieline--5ml .product-origin { font-size: 6.6px; }
  .dieline--5ml .col--ingredients { left: 166px; top: 6px; width: 86px; font-size: 7.2px; }
  .dieline--5ml .col--ingredients h3 { font-size: 7.5px; }
  .dieline--5ml .col--about { left: 256px; top: 8px; width: 76px; font-size: 8.4px; }
</style>
</head>
<body>

<section class="dieline dieline--15ml" aria-label="15 mL dropper box layout">
  <div class="col col--ingredients">
    <h3>Ingredients:</h3>
    <p>Lavandula Angustifolia (Australian Lavender), Vetiveria Zizanoides (Vetiver) Root Oil, Sweet Vanilla Fragrant Oil, Pelargonium Capitatum (Cape Rose Geranium) Leaf Extract, Juniperus Virginiana (Cedarwood) Wood Oil, Citrus Limon (Australian Lemon) Peel Oil, Origanum Majorana (Marjoram) Leaf Oil, Cananga Odorata (Ylang Ylang) Flower Oil, Anthemis Nobilis (Roman Chamomile) Flower Oil</p>
  </div>
  <div class="wordmark">DUSK HAVEN</div>
  <div class="info-panel">
    <div class="info-panel__story">
      <p>Essential Oils have been used for centuries to help prepare the mind and body for sleep.</p>
      <p>Add Dusk Haven to your nightly bedtime ritual to help support you in achieving deep and rejuvenating sleep.</p>
    </div>
    <div class="info-panel__product">
      <div class="product-title">Essential Oil Blend</div>
      <div class="product-sub">made with Lavender, Vetiver, Cedarwood, Marjoram and Roman Chamomile</div>
      <div class="product-origin">Made in Australia<br>1/2 fl.oz./15 mL</div>
    </div>
  </div>
  <div class="brand-dot"></div>
  <div class="col col--directions">
    <h3>Directions:</h3>
    <p><b>Apply directly onto skin. For sensitive skin, dilute with a carrier oil (such as jojoba or coconut) before application.</b></p>
    <p><b>Diffuse</b>Add 4-6 drops to a diffuser or oil burner at night to create a calm and grounded environment.</p>
    <p><b>Bathe</b>Add 2-4 drops to a warm bath to help calm the body and mind.</p>
    <p><b>Inhale</b>Place 2 drops in the palms of the hands and inhale directly to ease you into a restful sleep.</p>
    <p><b>Massage</b>Dilute 4 drops with a carrier oil (such as jojoba or coconut), and massage into the feet before sleep.</p>
    <p style="margin-top:22px;font-size:9.5px">Visit<br><strong>www.duskhaven.com.au</strong><br><strong>@duskhavenau</strong><br>to learn more</p>
  </div>
  <div class="col col--about">
    <p>Dusk Haven contain a balanced blend of the most sleep supporting essential oils, renowned for their grounding and calming properties.</p>
    <div class="notes" style="margin-top:10px">
      <p><i>Lavender</i>for restfulness</p>
      <p><i>Vetiver</i>for grounding</p>
      <p><i>Cedarwood</i>for relaxation</p>
      <p><i>Marjoram</i>for balance</p>
      <p><i>Roman Chamomile</i>for comfort</p>
    </div>
    <span class="brand-dot"></span>
    <p class="caution" style="font-size:9.5px">CAUTION:<br>Possible skin sensitivity. Keep out of reach of children. Not for ingestion or internal use. Avoid contact with eyes, inner ears and sensitive areas.</p>
    <div class="marks" style="margin:8px 0 4px"><span class="mark-recycle" style="width:18px;height:18px"></span><span class="mark-open" style="width:18px;height:16px"></span></div>
    <p>1/2 fl.oz./15 mL</p>
  </div>
</section>

<section class="dieline dieline--10ml" aria-label="10 mL roll-on box layout">
  <div class="col col--directions">
    <h3>Directions:</h3>
    <p>Apply directly onto skin. For sensitive skin, dilute with a carrier oil (such as jojoba or coconut) before application.</p>
    <p style="margin-top:12px;font-size:8.5px">Visit<br><strong>duskhaven.com.au</strong><br><strong>@duskhavenau</strong><br>to learn more</p>
  </div>
  <div class="wordmark">DUSK HAVEN</div>
  <div class="info-panel">
    <div class="info-panel__story">
      <p>Essential Oils have been used for centuries to help prepare the mind and body for sleep.</p>
      <p>Add Dusk Haven to your nightly bedtime ritual to help support you in achieving deep and juvenating sleep.</p>
    </div>
    <div class="info-panel__product">
      <div class="product-sub" style="font-size:10px">Roll on</div>
      <div class="product-title">Essential Oil Blend</div>
      <div class="product-sub">made with Lavender, Vetiver, Cedarwood, Marjoram and Roman Chamomile</div>
      <div class="product-origin">Made in Australia<br>0,34 fl.oz./10 mL</div>
    </div>
  </div>
  <div class="brand-dot"></div>
  <div class="col col--ingredients">
    <h3>Ingredients:</h3>
    <p>Lavandula Angustifolia (Australian Lavender), Vetiveria Zizanoides (Vetiver) Root Oil, Sweet Vanilla Fragrant Oil, Pelargonium Capitatum (Cape Rose Geranium) Leaf Extract, Juniperus Virginiana (Cedarwood) Wood Oil, Citrus Limon (Australian Lemon) Peel Oil, Origanum Majorana (Marjoram) Leaf Oil, Cananga Odorata (Ylang Ylang) Flower Oil, Anthemis Nobilis (Roman Chamomile) Flower Oil</p>
    <p class="caution" style="margin-top:8px;font-size:8.6px">CAUTION: Possible skinsensitivity. Keep out of reach of children. Not for ingestion or internal use. Avoid contact with eyes, inner ears and sensitive areas.</p>
  </div>
  <div class="col col--about">
    <p>Dusk Haven contain a balanced blend of the most sleep supporting essential oils, renowned for their grounding and calming properties.</p>
    <div class="notes" style="margin-top:10px">
      <p><i>Lavender</i>for restfulness</p>
      <p><i>Vetiver</i>for grounding</p>
      <p><i>Cedarwood</i>for relaxation</p>
      <p><i>Marjoram</i>for balance</p>
      <p><i>Roman Chamomile</i>for comfort</p>
    </div>
    <div class="marks" style="margin:22px 0 4px"><span class="mark-recycle" style="width:22px;height:22px"></span><span class="mark-open" style="width:22px;height:20px"></span></div>
    <p style="font-size:8.5px">0,34 fl.oz./10 mL</p>
  </div>
</section>

<section class="dieline dieline--5ml" aria-label="5 mL roll-on box layout">
  <div class="col col--directions">
    <h3>Directions:</h3>
    <p>Apply directly onto skin. For sensitive skin, dilute with a carrier oil (such as jojoba or coconut) before application.</p>
    <p style="margin-top:6px;font-size:6.6px">Visit<br><strong>duskhaven.com.au</strong><br><strong>@duskhavenau</strong><br>to learn more</p>
  </div>
  <div class="wordmark">DUSK HAVEN</div>
  <div class="info-panel">
    <div class="info-panel__story">
      <p>Essential Oils have been used for centuries to help prepare the mind and body for sleep.</p>
      <p>Add Dusk Haven to your nightly bedtime ritual to help support you in achieving deep and juvenating sleep.</p>
    </div>
    <div class="info-panel__product">
      <div class="product-sub" style="font-size:8px">Roll on</div>
      <div class="product-title">Essential Oil Blend</div>
      <div class="product-sub">made with Lavender, Vetiver, Cedarwood, Marjoram and Roman Chamomile</div>
      <div class="product-origin">Made in Australia<br>0,17 fl.oz./5 mL</div>
    </div>
  </div>
  <div class="brand-dot"></div>
  <div class="col col--ingredients">
    <h3>Ingredients:</h3>
    <p>Lavandula Angustifolia (Australian Lavender), Vetiveria Zizanoides (Vetiver) Root Oil, Sweet Vanilla Fragrant Oil, Pelargonium Capitatum (Cape Rose Geranium) Leaf Extract, Juniperus Virginiana (Cedarwood) Wood Oil, Citrus Limon (Australian Lemon) Peel Oil, Origanum Majorana (Marjoram) Leaf Oil, Cananga Odorata (Ylang Ylang) Flower Oil, Anthemis Nobilis (Roman Chamomile) Flower Oil</p>
    <p class="caution" style="margin-top:6px;font-size:6.4px">CAUTION: Possible skinsensitivity. Keep out of reach of children. Not for ingestion or internal use. Avoid contact with eyes, inner ears and sensitive areas.</p>
  </div>
  <div class="col col--about">
    <p>Dusk Haven contain a balanced blend of the most sleep supporting essential oils, renowned for their grounding and calming properties.</p>
    <div class="notes" style="margin-top:6px">
      <p style="margin-bottom:1px"><i>Lavender</i>for restfulness</p>
      <p style="margin-bottom:1px"><i>Vetiver</i>for grounding</p>
      <p style="margin-bottom:1px"><i>Cedarwood</i>for relaxation</p>
      <p style="margin-bottom:1px"><i>Marjoram</i>for balance</p>
      <p style="margin-bottom:1px"><i>Roman Chamomile</i>for comfort</p>
    </div>
    <div class="marks" style="margin:8px 0 3px"><span class="mark-recycle" style="width:16px;height:16px"></span><span class="mark-open" style="width:16px;height:14px"></span></div>
    <p style="font-size:7px">0,17 fl.oz./5 mL</p>
  </div>
</section>

</body>
</html>
```